Ads for Law Firm

I am an employment lawyer who represents individual employees. I currently have a banner ad on sites focused on individual employment rights, like StaffLedgerHub.org and TallpineGuidance.com. I am looking for an ad that incorporates best practices for promoting a professional service.

I am attaching a couple of existing ads that I want to replace. The new ad should be the same dimension as the attached. The old ad is a friend helped with, and focuses on my great credentials.

I have read that people looking for lawyers care a less about credentials, and more about whether the lawyer can protect them. It should also have a call to action, being to call or email me. Therefore, the ad should say something like "call [me/Toby] to protect your [job/employment/rights/etc],"

Lawyer

```html
<!DOCTYPE html>
<html lang="en">
<head>
<meta charset="utf-8">
<title>Toby Halvorsen – Employment Lawyer Banner</title>
<link href="https://fonts.googleapis.com/css2?family=PT+Sans:wght@400;700&display=swap" rel="stylesheet">
<style>
  :root {
    --wood-light: #c98a4e;
    --wood-mid: #b8733a;
    --wood-dark: #8f5226;
    --band-top-light: #f4f7fa;
    --band-top-mid: #c9d3dc;
    --band-top-dark: #7d8a96;
    --band-bottom: #1c1e20;
    --band-bottom-edge: #3a3d40;
    --ink-dark: #111418;
    --ink-light: #ffffff;
    --cta-bg: #e6f0f8;
    --arrow: #3b4046;
    --photo-tone: #b9a79a;
  }
  html, body {
    margin: 0;
    padding: 0;
    width: 1200px;
    height: 1000px;
    overflow: hidden;
  }
  .backdrop {
    position: relative;
    width: 1200px;
    height: 1000px;
    background:
      repeating-linear-gradient(90deg, rgba(0,0,0,0.06) 0 1px, transparent 1px 70px),
      radial-gradient(ellipse at 50% 45%, var(--wood-light) 0%, var(--wood-mid) 60%, var(--wood-dark) 100%);
    font-family: "PT Sans", sans-serif;
  }
  .banner {
    position: absolute;
    left: 384px;
    top: 424px;
    width: 468px;
    height: 60px;
    display: flex;
    border: 1px solid var(--band-bottom);
    box-sizing: border-box;
    overflow: hidden;
  }
  .banner__photo {
    width: 72px;
    height: 100%;
    background: linear-gradient(180deg, #d9cfc6 0%, var(--photo-tone) 55%, #3a3f4a 100%);
    flex: none;
  }
  .banner__body {
    width: 349px;
    flex: none;
    display: flex;
    flex-direction: column;
    position: relative;
  }
  .banner__name {
    height: 26px;
    margin: 0;
    background: linear-gradient(180deg, var(--band-top-light) 0%, var(--band-top-mid) 55%, var(--band-top-dark) 100%);
    color: var(--ink-dark);
    font-size: 19px;
    font-weight: 400;
    line-height: 27px;
    text-align: center;
    padding-right: 12px;
  }
  .banner__arrow {
    position: absolute;
    right: -4px;
    top: 2px;
  }
  .banner__message {
    flex: 1;
    display: flex;
    background: linear-gradient(180deg, var(--band-bottom-edge) 0%, var(--band-bottom) 100%);
    color: var(--ink-light);
    font-size: 11px;
    font-weight: 700;
    line-height: 13px;
    text-transform: uppercase;
    letter-spacing: -0.2px;
    white-space: nowrap;
  }
  .message-cell {
    padding: 3px 0 0 4px;
    box-sizing: border-box;
    overflow: hidden;
  }
  .message-cell--promise { width: 100px; }
  .message-cell--action { width: 143px; }
  .message-cell--specialty { width: 106px; }
  .banner__cta {
    flex: 1;
    background: var(--cta-bg);
    display: flex;
    align-items: center;
    justify-content: center;
    color: var(--ink-dark);
    text-decoration: none;
  }
  .banner__cta-label {
    display: block;
    transform: rotate(-90deg);
    font-size: 13px;
    font-weight: 700;
    line-height: 14px;
    white-space: nowrap;
    text-align: left;
  }
</style>
</head>
<body>
<div class="backdrop" role="img" aria-label="Warm wooden plank surface behind the banner">
  <div class="banner">
    <div class="banner__photo" role="img" aria-label="Portrait photo of attorney Toby Halvorsen"></div>
    <div class="banner__body">
      <h1 class="banner__name">TOBY HALVORSEN</h1>
      <svg class="banner__arrow" width="56" height="16" viewBox="0 0 56 16" aria-hidden="true">
        <path d="M2 4 Q4 10 12 10 L44 10" fill="none" stroke="var(--arrow)" stroke-width="4"/>
        <path d="M42 3 L54 10 L42 15 Z" fill="var(--arrow)"/>
      </svg>
      <div class="banner__message">
        <div class="message-cell message-cell--promise">Protect your<br>job today</div>
        <div class="message-cell message-cell--action">Call Toby to guard<br>your employment</div>
        <div class="message-cell message-cell--specialty">Ohio Employment<br>Law Specialist</div>
      </div>
    </div>
    <a class="banner__cta" href="#contact"><span class="banner__cta-label">EMAIL<br>ME.</span></a>
  </div>
</div>
</body>
</html>
```